Childrens Business Card Design Project

We have an existing logo attached which we'd like to use as part of our new business card design.

The design needs to be relatively gender neutral and contain bright colours.

In terms of look and feel think:

Fun, Modern, Quality (as opposed to cheap!) and of course Party!

Single or double sided - i am not decided on either one yet - ideally i'd like to see designs for both because if you think stylistically it would benefit having two sides then please try it out!

I think the challenge here is finding a really good background colour (if you think it needs one) and also choosing an eye grabbing text that compliments the existing logo - do that an you are onto a winner! I have another image for the business (which i have attached) which uses stripes so i am keen to see a design that incorporates this to tie in all my collateral.

The copy required is as follows (not necesarily in this order)

Bookings/Enquiries:

Tilda

T: 0498 217 503
E: enquiries@brightfoxparties.example.au

ABN: 47 302 658 114

Any feedback on text is welcomed - please message me or add to the discussion.

Reason: Hi All, I have received some promising designs, but overall i am not impressed with the quality of the work so have extended the deadline as this project has been committed. I will aim to attach some business card examples to the brief tomorrow to give further guidance as a whole but please do not submit any designs on a generic background that are not related to the theme, have been carelessly placed with overlapping elements - it just looks sloppy. For those who have read the brief an incorporated stripes or even spots this is on target as it convey's a party theme, however please work on getting the colours for the contact details by either a bold solid strip to highlight or some other way to frame it. When it comes to the logo, some people have removed the characters all together and changed the colour of the wording - this is fine. Also feel free to balloons starts - but keep it classy and watch your placement of these. I hope this helps and for the designs i would like to see revisions for i will aim to get back to you individually over the next day or so. Many thanks all.

Target Market(s)

Mothers in the suburbs of Australia with a disposal able income, children aged between 1-7 years old.

Industry/Entity Type

Business

Requirements
Must have
• The font and wording positioning must compliment the logo.

```html
<!DOCTYPE html>
<html lang="en">
<head>
<meta charset="utf-8">
<title>Brightfox Business Card</title>
<link href="https://fonts.googleapis.com/css2?family=Jost:wght@400&family=Sniglet:wght@400;800&display=swap" rel="stylesheet">
<style>
  :root {
    --page-bg: #eef1f3;
    --stripe-teal: #5cc5d6;
    --stripe-white: #ffffff;
    --band-teal: #4fbccd;
    --band-stripe: #5fc7d7;
    --logo-blue: #1f7fc6;
    --text-white: #ffffff;
    --fairy-tone: #e7737a;
    --clown-tone: #f2c64a;
    --pirate-tone: #7aa5cf;
  }
  * { margin: 0; padding: 0; box-sizing: border-box; }
  html, body {
    width: 1200px; height: 960px; overflow: hidden;
    background: var(--page-bg);
  }
  .business-card {
    position: absolute; left: 100px; top: 175px;
    width: 1000px; height: 610px;
    overflow: hidden;
    background: repeating-linear-gradient(90deg,
      var(--stripe-white) 0 14px, var(--stripe-teal) 14px 26px,
      var(--stripe-white) 26px 44px, var(--stripe-teal) 44px 52px,
      var(--stripe-white) 52px 64px, var(--stripe-teal) 64px 80px);
    box-shadow: 0 18px 40px rgba(20, 50, 60, 0.25);
  }
  .character {
    position: absolute;
    border-radius: 40px;
  }
  .character-fairy {
    left: 225px; top: 55px; width: 155px; height: 180px;
    background: linear-gradient(180deg, #8fd6c8, var(--fairy-tone));
  }
  .character-clown {
    left: 445px; top: 25px; width: 120px; height: 210px;
    background: linear-gradient(180deg, #e65a4f, var(--clown-tone) 45%, #78c24a);
  }
  .character-pirate {
    left: 680px; top: 70px; width: 130px; height: 165px;
    background: linear-gradient(180deg, #e54a3c, var(--pirate-tone) 55%, #7b5233);
  }
  .contact-band {
    position: absolute; left: 0; top: 0; width: 1000px; height: 610px;
  }
  .brand-name {
    position: absolute; left: 0; right: 0; top: 250px;
    text-align: center;
    font-family: "Sniglet", sans-serif; font-weight: 800;
    font-size: 84px; line-height: 1; letter-spacing: 10px;
    color: var(--logo-blue);
  }
  .contact-details {
    position: absolute; left: 0; right: 0; top: 388px;
    text-align: center; color: var(--text-white);
    font-family: "Jost", sans-serif;
  }
  .tagline {
    font-family: "Sniglet", sans-serif; font-weight: 400;
    font-size: 22px; letter-spacing: 3px; line-height: 30px;
  }
  .contact-name { font-size: 32px; line-height: 38px; }
  .contact-role { font-size: 26px; line-height: 34px; }
  .contact-line {
    font-size: 27px; line-height: 36px;
    display: flex; justify-content: center; align-items: center; gap: 8px;
  }
  .contact-line svg { flex: none; }
  .abn { font-size: 22px; line-height: 30px; }
</style>
</head>
<body>
  <div class="business-card">
    <div class="character character-fairy" role="img" aria-label="Illustration of a smiling fairy in a red dress with a wand"></div>
    <div class="character character-clown" role="img" aria-label="Illustration of a clown doing a handstand"></div>
    <div class="character character-pirate" role="img" aria-label="Illustration of a little pirate with a sword"></div>

    <svg class="contact-band" viewBox="0 0 1000 610" aria-hidden="true">
      <defs>
        <pattern id="band-stripes" width="60" height="610" patternUnits="userSpaceOnUse">
          <rect x="0" y="0" width="14" height="610" fill="var(--band-stripe)"/>
          <rect x="30" y="0" width="8" height="610" fill="var(--band-stripe)"/>
        </pattern>
      </defs>
      <path d="M0 385 Q500 325 1000 385 L1000 610 L0 610 Z" fill="var(--band-teal)"/>
      <path d="M0 385 Q500 325 1000 385 L1000 610 L0 610 Z" fill="url(#band-stripes)" opacity="0.6"/>
    </svg>

    <div class="brand-name">Brightfox</div>

    <div class="contact-details">
      <p class="tagline">Kids Parties &amp; Events</p>
      <p class="contact-name">Tilda</p>
      <p class="contact-role">Bookings/Enquiries</p>
      <p class="contact-line">
        <svg width="16" height="26" viewBox="0 0 16 26" aria-hidden="true">
          <rect x="1.5" y="1.5" width="13" height="23" rx="2.5" fill="none" stroke="#fff" stroke-width="2.5"/>
          <circle cx="8" cy="20.5" r="1.6" fill="#fff"/>
        </svg>
        <span>0498 217 503</span>
      </p>
      <p class="contact-line">
        <svg width="30" height="22" viewBox="0 0 30 22" aria-hidden="true">
          <rect x="1.5" y="1.5" width="27" height="19" fill="none" stroke="#fff" stroke-width="2.5"/>
          <path d="M2 2 L15 13 L28 2" fill="none" stroke="#fff" stroke-width="2.5"/>
        </svg>
        <span>enquiries@brightfoxparties.example.au</span>
      </p>
      <p class="abn">ABN: 47 302 658 114</p>
    </div>
  </div>
</body>
</html>
```